General brochure with course listing

A general brochure for the Global Statute Academy, about 40 A5 pages that includes mission, vision, history, descriptions of our technical assistance and capacity building programming and detailed descriptions of our courses. Would be for both online pdf (magazine style) and print. I have attached an example of an older one that was satisfactory but not as professional as what we're looking for now.

Target Market(s)

Lawyers and government officials around the world.

Industry/Entity Type

Legal and capacity building

Requirements
Must have
• A good design and template that we can replicate on our own in InDesign annually. We need the layout from you and we will provide the copy. We will also publish as a pdf
Nice to have
• Colors and branding from our website - www.gsa-learn.org

```html
<!DOCTYPE html>
<html lang="en">
<head>
<meta charset="utf-8">
<title>Global Statute Academy – Why the GSA?</title>
<link href="https://fonts.googleapis.com/css2?family=Questrial&display=swap" rel="stylesheet">
<style>
  :root {
    --accent: #e2552b;
    --ink: #2b2b2b;
    --body: #3a3a3a;
    --paper: #ffffff;
  }
  * { margin: 0; padding: 0; box-sizing: border-box; }
  html, body { width: 1200px; height: 423px; overflow: hidden; background: var(--paper); }
  .spread {
    position: relative; width: 1200px; height: 423px;
    font-family: "Questrial", "Helvetica Neue", Arial, sans-serif;
    color: var(--body);
  }
  .section-title {
    position: absolute; left: 37px; top: 36px;
    font-size: 13.5px; letter-spacing: 1.4px; font-weight: 400;
    color: var(--accent);
  }
  .hero-photo {
    position: absolute; left: 0; top: 122px; width: 386px; height: 191px;
    background:
      radial-gradient(ellipse at 70% 55%, rgba(60,70,110,0.55), transparent 60%),
      linear-gradient(90deg, #c7b3a6 0%, #9e8b82 22%, #6c5a55 45%, #3c2b2a 70%, #2a1d1e 100%);
  }
  .reason { position: absolute; top: 60px; width: 169px; }
  .reason-number {
    font-size: 28px; line-height: 1; color: var(--ink); font-weight: 400;
    height: 26px; margin-top: 4px;
  }
  .reason-rule { width: 44px; height: 1.2px; background: var(--ink); margin-top: 6px; }
  .reason-rule.wide { width: 50px; }
  .reason-heading {
    margin-top: 24px; font-size: 16.5px; font-weight: 400; color: var(--accent);
    line-height: 1.2; white-space: nowrap;
  }
  .reason-text {
    margin-top: 13px; font-size: 8.9px; line-height: 14.2px;
    text-align: justify; hyphens: auto; height: 156px; overflow: hidden;
  }
  .reason-icon { position: absolute; top: 270px; left: 0; width: 34px; height: 30px; }
  .reason-icon svg { width: 100%; height: 100%; fill: none; stroke: var(--accent); stroke-width: 1.3; stroke-linejoin: round; stroke-linecap: round; }
  .folio { position: absolute; top: 399px; font-size: 9px; color: var(--ink); }
  .folio-rule { position: absolute; top: 405px; height: 1px; background: var(--accent); }
</style>
</head>
<body>
<main class="spread">
  <h1 class="section-title">WHY THE GSA?</h1>

  <div class="hero-photo" role="img" aria-label="Photograph of professionals seated in a row in a lecture hall, one woman looking toward the camera"></div>

  <section class="reason" style="left:398px">
    <div class="reason-number">01</div>
    <div class="reason-rule wide"></div>
    <h2 class="reason-heading">Professional Contacts</h2>
    <p class="reason-text">Agniet erum hil evenitiant. Maionsed quia dia volesti onsedipsunde volupta non et hitatqu idelia suntia voluptam ius nonecaborro doloritam nos aut quunto cus dolupta testio tectas autenest, nobisseque rerum iunt rem nonsedignat. gniet erum hil evenitiant. Maionsed quia dia volesti onsedipsunde volupta non et hitatqu idelia suntia voluptam ius nonecaborro doloritam nos aut quunto cus dolupta testio tectas autenest, nobisseque rerum iunt</p>
    <div class="reason-icon">
      <svg viewBox="0 0 34 30" aria-hidden="true">
        <path d="M1 10 L8 3 L13 7 L9 11"/>
        <path d="M33 10 L26 3 L19 6 L13 11 L16 13 L21 9"/>
        <path d="M3 12 L14 25 C16 27 18 26 17 24"/>
        <path d="M31 12 L19 26 C17 28 14 27 14 25"/>
        <path d="M10 17 L16 23 M12 15 L19 22 M15 13 L22 20"/>
      </svg>
    </div>
  </section>

  <section class="reason" style="left:641px">
    <div class="reason-number">02</div>
    <div class="reason-rule"></div>
    <h2 class="reason-heading">Quality Training</h2>
    <p class="reason-text">Agniet erum hil evenitiant. Maionsed quia dia volesti onsedipsunde volupta non et hitatqu idelia suntia voluptam ius nonecaborro doloritam nos aut quunto cus dolupta testio tectas autenest, nobisseque rerum iunt rem nonsedignat. Agniet erum hil evenitiant. Maionsed quia dia volesti onsedipsunde volupta non et hitatqu idelia suntia voluptam ius nonecaborro doloritam nos aut quunto cus dolupta testio tectas autenest, nobisseque rerum iunt</p>
    <div class="reason-icon">
      <svg viewBox="0 0 34 30" aria-hidden="true">
        <path d="M15 1 L18 4 L22 3 L23 7 L27 8 L26 12 L29 15 L26 18 L27 22 L23 23 L22 27 L18 26 L15 29 L12 26 L8 27 L7 23 L3 22 L4 18 L1 15 L4 12 L3 8 L7 7 L8 3 L12 4 Z"/>
        <path d="M13 11 L16 9 L16 20 M13 20 L19 20"/>
      </svg>
    </div>
  </section>

  <section class="reason" style="left:821px">
    <div class="reason-number">03</div>
    <div class="reason-rule"></div>
    <h2 class="reason-heading">Faculty</h2>
    <p class="reason-text">tempe reria deliam, volecti ssusam dem sit ipic totatqui sint quoditatur? Daesequam sandi odis magnatatus pero volorrum voluptae et aliqui sum delloreicid modipide et ommolorion consedi seque volupta turibuscidem hit omniatum il is maio quat. Agniet erum hil evenitiant. Maionsed quia dia volesti onsedipsunde volupta non et hitatqu idelia suntia voluptam ius nonecaborro doloritam nos aut quunto cus dolupta testio tectas autenest, nobisseque</p>
    <div class="reason-icon">
      <svg viewBox="0 0 34 30" aria-hidden="true">
        <path d="M1 10 L17 3 L33 10 L17 17 Z"/>
        <path d="M7 13 L7 25 L27 25 L27 13"/>
        <path d="M7 20 L17 24 L27 20"/>
        <path d="M17 10 L4 13 L4 20"/>
        <circle cx="17" cy="10" r="1.2"/>
      </svg>
    </div>
  </section>

  <section class="reason" style="left:1003px">
    <div class="reason-number">04</div>
    <div class="reason-rule"></div>
    <h2 class="reason-heading">Location</h2>
    <p class="reason-text">tempe reria deliam, volecti ssusam dem sit ipic totatqui sint quoditatur? Daesequam sandi odis magnatatus pero volorrum voluptae et aliqui sum delloreicid modipide et ommolorion consedi seque volupta turibuscidem hit omniatum il is maio quat. Agniet erum hil evenitiant. Maionsed quia dia volesti onsedipsunde volupta non et hitatqu idelia suntia voluptam ius nonecaborro doloritam nos aut quunto cus dolupta testio tectas autenest, nobisseque</p>
    <div class="reason-icon">
      <svg viewBox="0 0 34 30" aria-hidden="true">
        <circle cx="13" cy="12" r="9"/>
        <ellipse cx="13" cy="12" rx="4" ry="9"/>
        <path d="M4 12 L22 12 M6 7 L20 7 M6 17 L20 17"/>
        <path d="M3 4 C-2 12 3 22 13 23 C17 23 20 22 22 20"/>
        <path d="M13 23 L13 26 M8 28 L18 28 M10 26 L16 26"/>
      </svg>
    </div>
  </section>

  <span class="folio" style="left:45px">8</span>
  <div class="folio-rule" style="left:61px; width:505px"></div>
  <div class="folio-rule" style="left:641px; width:506px"></div>
  <span class="folio" style="left:1154px">9</span>
</main>
</body>
</html>
```